Research Report on Media Literacy Needs a Design

We've got a cool story to tell about an innovative process of teacher professional development in media literacy education. We have a 20 page report about the work. We're looking for a designer to give it a simple but attractive look so we can publish it online.

Teacher

```html
<!DOCTYPE html>
<html lang="en">
<head>
<meta charset="utf-8">
<title>Executive Summary – Media and Information Literacy</title>
<link rel="stylesheet" href="https://fonts.googleapis.com/css2?family=Lato:wght@300;400&display=swap">
<style>
  :root {
    --brand-blue: #3498d3;
    --ink: #1f1f1f;
    --paper: #ffffff;
  }
  * { margin: 0; padding: 0; box-sizing: border-box; }
  html, body { width: 927px; height: 1200px; overflow: hidden; background: var(--paper); }
  .page {
    position: relative;
    width: 927px;
    height: 1200px;
    overflow: hidden;
    font-family: "Lato", Arial, sans-serif;
    color: var(--ink);
  }
  .section-banner {
    position: absolute;
    left: 0; top: 0;
  }
  .section-title {
    position: absolute;
    font-family: "Lato", Arial, sans-serif;
    font-weight: 300;
    font-size: 66px;
    line-height: 1;
    color: var(--paper);
    letter-spacing: 0.5px;
    white-space: nowrap;
  }
  .title-summary { left: 62px; top: 150px; }
  .title-background { left: 173px; top: 741px; }
  .body-copy {
    position: absolute;
    left: 66px;
    width: 800px;
    font-size: 14.2px;
    line-height: 19.7px;
  }
  .body-copy p + p { margin-top: 19px; }
  .copy-summary { top: 291px; }
  .copy-background { top: 880px; }
  .num { color: var(--brand-blue); }
  .page-footer {
    position: absolute;
    left: 9px;
    right: 0;
    top: 1155px;
    height: 20px;
    display: flex;
    align-items: center;
  }
  .page-number {
    background: var(--brand-blue);
    color: var(--paper);
    font-size: 14px;
    padding: 1px 6px;
    line-height: 17px;
  }
  .running-title {
    color: var(--brand-blue);
    font-size: 15px;
    letter-spacing: 0.6px;
    margin-left: 8px;
    white-space: nowrap;
  }
  .footer-rule {
    flex: 1;
    height: 1px;
    background: var(--brand-blue);
    margin-left: 3px;
    margin-top: 8px;
  }
</style>
</head>
<body>
<div class="page">
  <svg class="section-banner" width="927" height="1200" viewBox="0 0 927 1200" aria-hidden="true">
    <polygon points="0,137 25,114 813,114 813,223 788,248 0,248" fill="var(--brand-blue)"/>
    <polygon points="114,732 140,707 927,707 927,843 114,843" fill="var(--brand-blue)"/>
    <polygon points="902,843 927,818 927,843" fill="var(--paper)"/>
  </svg>

  <h1 class="section-title title-summary">Executive Summary</h1>
  <div class="body-copy copy-summary">
    <p>Media and information literacy are essential competencies that can be activated and developed through a variety of innovative forms of learning and teaching. This report describes a year-long professional development program developed and implemented by Linden Hill School faculty during the 2013 – 2014 academic year in collaboration with the Media Learning Studio at the Calloway School of Communication and Media, Northshore State University. The goal of the initiative was designed to build coherence, quality, effectiveness and vision around media and information literacy integration at Linden Hill School across subjects and grade levels. The process was informed by faculty development work previously described in Avery and Stone's Exploring Media Literacy but it also included elements unique to the context of Linden Hill School. The professional development program included a 6-stage process that activated faculty as learners in a dynamic inquiry process.</p>
    <p>Key elements of the professional development program included: <span class="num">(1)</span> reflecting on faculty motivations and values in using digital media and technology; <span class="num">(2)</span> expanding the concept of literacy and identifying learning targets; <span class="num">(3)</span> considering the value of both formal and informal media and information literacy (MIL) learning; <span class="num">(4)</span> conducting teaching-partner interviews as a paradigm for collaborative professional development; <span class="num">(5)</span> using MIL tagging to support a professional development learning community; <span class="num">(6)</span> sharing with the whole school community. Using a seminar-style approach to professional development, faculty worked collaboratively to develop shared knowledge and understanding of how children develop MIL competencies within the current context of curriculum and instruction at Linden Hill School. This process also enabled the faculty to imagine potential future directions for the program.</p>
  </div>

  <h2 class="section-title title-background">Background &amp; Context</h2>
  <div class="body-copy copy-background">
    <p>Linden Hill School has a long history of developing and supporting media and information literacy (MIL) integration into student learning and professional development. For over a decade, the approach to professional development at Linden Hill School has consisted of experts providing definitions and frameworks for MIL that capture the variety of theoretical and pedagogical approaches in the practice of media literacy education and digital learning.</p>
    <p>In 2012-2013, Linden Hill School commissioned a program review from Project Clear View at Westbrook College, whose report noted that Linden Hill School has “potential to be a groundbreaking model [in media and information literacy] for the U.S.” The report identified certain gaps in teacher knowledge of and approaches to media and information literacy as it pertained to instruction and learning at Linden Hill School. Some confusion around MIL among faculty was due to lack of pedagogical or technological knowledge, but more was simply a result of faculty isolation—many were simply unaware of the high-quality lessons and projects that other</p>
  </div>

  <footer class="page-footer">
    <span class="page-number">Pg 02</span>
    <span class="running-title">MEDIA AND INFORMATION LITERACY</span>
    <span class="footer-rule"></span>
  </footer>
</div>
</body>
</html>
```